Business Card for Inovative Flexible Packaging Company

Create a business card that is both simple and stricking at the same time.
Preferably only one color (orange) or two colors (black and orange).
Information to print:
Torvalo, Lda
[T] 22 418 6093
[M] 91 326 7041
[F] 22 418 6135
[@] torvalo.ac@correiomx.com
SEDE & ARMAZÉM
Rua Das Figueiras do Monte, 312
Vilar do Monte
4410-832 Vilar do Monte - Vale Norte
PORTUGAL
Reason: A lot of the ideas are obvious. I want something different. Inovative. dare to do something eye catching with style.
Business Consumers. Packaging Designers.
Business

```html
<!DOCTYPE html>
<html lang="pt">
<head>
<meta charset="utf-8">
<title>Torvalo — Business Card</title>
<link rel="stylesheet" href="https://fonts.googleapis.com/css2?family=Lora:wght@400;700&display=swap">
<style>
  :root {
    --backdrop: #ececee;
    --card: #ffffff;
    --orange: #f24f12;
    --ink: #111111;
    --grey: #4a4a4a;
    --shadow: rgba(0,0,0,0.45);
  }
  * { margin: 0; padding: 0; box-sizing: border-box; }
  html, body { width: 1200px; height: 900px; overflow: hidden; }
  body {
    position: relative;
    background: var(--backdrop);
    font-family: "Lora", Georgia, serif;
    color: var(--ink);
  }
  .card {
    position: absolute;
    top: 177px;
    width: 544px;
    height: 312px;
    background: var(--card);
    box-shadow: 6px 4px 8px var(--shadow);
    overflow: hidden;
  }
  .card--front { left: 48px; }
  .card--back { left: 633px; width: 539px; }

  .brand { position: absolute; display: flex; align-items: center; }
  .brand__square { background: var(--orange); flex: none; }
  .brand__text { display: flex; flex-direction: column; }
  .brand__name { color: var(--orange); font-weight: 700; line-height: 1; }
  .brand__tagline { color: var(--grey); letter-spacing: 0.26em; white-space: nowrap; line-height: 1; }

  .card--front .brand { left: 110px; top: 104px; }
  .card--front .brand__square { width: 68px; height: 68px; margin-right: 14px; }
  .card--front .brand__name { font-size: 58px; }
  .card--front .brand__tagline { font-size: 10px; margin-top: 6px; }

  .accent-bar { position: absolute; left: 0; top: 0; width: 12px; height: 100%; background: var(--orange); }
  .accent-rule { position: absolute; left: 12px; bottom: 0; width: 100%; height: 3px; background: var(--ink); }

  .card--back .brand { left: 34px; top: 22px; }
  .card--back .brand__square { width: 46px; height: 46px; margin-right: 10px; }
  .card--back .brand__name { font-size: 38px; }
  .card--back .brand__tagline { font-size: 8px; margin-top: 4px; }

  .company { position: absolute; left: 42px; top: 128px; font-size: 18px; font-weight: 400; }
  .contacts { position: absolute; left: 42px; top: 162px; list-style: none; font-size: 15px; }
  .contacts li { display: flex; align-items: center; height: 23px; }
  .contacts svg { width: 12px; height: 12px; margin-right: 6px; fill: var(--orange); flex: none; }
  .address { position: absolute; left: 274px; top: 154px; font-size: 15px; line-height: 20.5px; font-style: normal; }

  .signature-mark { left: 826px; top: 786px; }
  .signature-mark .brand__square { width: 84px; height: 84px; margin-right: 16px; }
  .signature-mark .brand__name { font-size: 62px; }
  .signature-mark .brand__tagline { font-size: 10px; margin-top: 6px; color: var(--orange); }
</style>
</head>
<body>

  <section class="card card--front" aria-label="Card front">
    <div class="brand">
      <span class="brand__square"></span>
      <div class="brand__text">
        <span class="brand__name">torvalo</span>
        <span class="brand__tagline">FLEXIBLE WRAP SYSTEMS</span>
      </div>
    </div>
  </section>

  <section class="card card--back" aria-label="Card back">
    <span class="accent-bar"></span>
    <span class="accent-rule"></span>

    <div class="brand">
      <span class="brand__square"></span>
      <div class="brand__text">
        <span class="brand__name">torvalo</span>
        <span class="brand__tagline">FLEXIBLE WRAP SYSTEMS</span>
      </div>
    </div>

    <h1 class="company">Torvalo, Lda</h1>
    <ul class="contacts">
      <li><svg viewBox="0 0 24 24"><path d="M6.6 10.8a15 15 0 0 0 6.6 6.6l2.2-2.2c.3-.3.7-.4 1-.2 1.1.4 2.3.6 3.6.6.6 0 1 .4 1 1V20c0 .6-.4 1-1 1A17 17 0 0 1 3 4c0-.6.4-1 1-1h3.5c.6 0 1 .4 1 1 0 1.3.2 2.5.6 3.6.1.3 0 .7-.2 1z"/></svg>22 418 6093</li>
      <li><svg viewBox="0 0 24 24"><path d="M7 1h10a2 2 0 0 1 2 2v18a2 2 0 0 1-2 2H7a2 2 0 0 1-2-2V3a2 2 0 0 1 2-2zm0 3v13h10V4z"/></svg>91 326 7041</li>
      <li><svg viewBox="0 0 24 24"><path d="M6 2h9l3 3v5H6zM3 11h18v10H3zm3 3v2h3v-2zm5 0v2h3v-2zm5 0v2h3v-2z"/></svg>22 418 6135</li>
      <li><svg viewBox="0 0 24 24"><path d="M2 5h20v14H2zm2 2v.5l8 5 8-5V7z"/></svg>torvalo.ac@correiomx.com</li>
    </ul>

    <address class="address">
      SEDE &amp; ARMAZÉM<br>
      Rua Das Figueiras do Monte, 312<br>
      Vilar do Monte<br>
      4470-832 Vilar - Vale Norte<br>
      PORTUGAL
    </address>
  </section>

  <div class="brand signature-mark">
    <span class="brand__square"></span>
    <div class="brand__text">
      <span class="brand__name">torvalo</span>
      <span class="brand__tagline">FLEXIBLE WRAP SYSTEMS</span>
    </div>
  </div>

</body>
</html>
```